Inspiring book cover design (business book for designers and innovators)

I'm writing my first book, to be published early next year. I'm struggling to come up with an inspiring book cover design. I need your help!

Information to be included on the cover:
Book Title: Bright maker's manual
Subtitle: Designing products and services that make sense
Author: Marieke Vollen
Optional (not sure yet if I should include this on the cover): with online toolset

The book will be a square, size 170 x 170 mm
In the uploaded file you can find some example pages from the inside of the book. The cover design should fit with the design style of the example pages. The cover should "jump out" from the shelve in a bookstore and should attract designers, innovators, product managers, developers, and startup founders to buy the book.
Publisher: www.quarlomedia.example

About the book:
Why do some products fail while others become a success? Why do so many companies launch crappy products and services that nobody wants? This book is both a guide to and a source of inspiration for, designing products and services that make sense. Because if they make sense to people, people will want them.
In order for tech products and services to make sense, and create value for users, we need to apply technologies in a meaningful way. We can achieve this by designing strong benefits and at the same time minimizing resistance users might have against new technologies.
This book offers a complete overview of how to develop products and services that make sense: 27 ways to strengthen benefits and 28 ways to mitigate resistance. It offers practical insights, examples, tips, and tools to design products and services that people will love to use.

About the author:
https://www.profilehub.example/in/mariekevollen/

Target Market(s)

designers, innovators, product managers, developers, and startup founders

Industry/Entity Type

Design Agency

Font styles to use
Other font styles liked:
• You can choose. The inside of the book uses 3 fonts: LuloCleanW01-OneBold, Sansation, Segoe UI

Requirements
Must have
• Clean, yet creative design.
Square shape
Fits the design style of the example pages
Sans serif fonts. Do not have to be the same fonts like the ones that are used inside the book (LuloCleanW01-OneBold, Sansation, Segoe UI), but should go well with them.

Bright makers manual
48 ideas for building tools and services people truly want
Marieke Vollen
Nice to have
• I have several ideas that you might take as a starting point:
1) Do something with the left brain (rational, more digital) - right brain (creative, more emotional). For products to make sense, it needs to appeal to both parts of the brain
2) Work with a pattern, for example a (polygonal) triangular pattern
3) playful element in the letters, for example turning the O in innovator's into an on-off button or a stylish smiley, flipping the N in innovator's, doing something playful with the ' in innovator's
I've uploaded some images as a source of inspiration.

The cover should have a different color than the red/blue used in the example pages, but should fit the color palette that is used in the example pages.
Trigger curiosity.
Should not have
• Photographic pictures

```html
<!DOCTYPE html>
<html lang="en">
<head>
<meta charset="utf-8">
<title>Bright maker's manual — Marieke Vollen</title>
<link href="https://fonts.googleapis.com/css2?family=Montserrat:wght@300;500;600&display=swap" rel="stylesheet">
<style>
  :root {
    --ink-deep: #0a4f86;
    --ink-mid: #1470b4;
    --ink-light: #2a9ad8;
    --sub-ink: #1a6aa4;
    --author-ink: #2c8ac8;
    --bg-center: #ffffff;
    --bg-mid: #e3e9ed;
    --bg-edge: #b9c8d1;
    --block-top: #1a78cc;
    --block-bottom: #0c5bb0;
  }
  * { margin: 0; padding: 0; box-sizing: border-box; }
  html, body { width: 1200px; height: 1200px; overflow: hidden; }
  body { font-family: "Montserrat", Arial, sans-serif; }

  .cover {
    position: relative;
    width: 1200px;
    height: 1200px;
    overflow: hidden;
    background: radial-gradient(ellipse 75% 70% at 52% 46%, var(--bg-center) 0%, var(--bg-mid) 45%, var(--bg-edge) 100%);
  }

  .network-texture {
    position: absolute;
    inset: 0;
    background:
      radial-gradient(ellipse 40% 50% at 0% 30%, rgba(160,185,200,0.35), transparent 70%),
      radial-gradient(ellipse 40% 40% at 100% 10%, rgba(190,195,200,0.4), transparent 70%);
  }

  .author {
    position: absolute;
    top: 46px;
    left: 0;
    width: 100%;
    text-align: center;
    font-weight: 300;
    font-size: 47px;
    letter-spacing: 1px;
    color: var(--author-ink);
  }

  .title {
    position: absolute;
    right: 210px;
    top: 452px;
    text-align: right;
  }
  .title-line {
    display: block;
    font-weight: 600;
    font-size: 116px;
    line-height: 96px;
    letter-spacing: -1px;
    background: linear-gradient(90deg, var(--ink-deep) 0%, var(--ink-mid) 50%, var(--ink-light) 100%);
    -webkit-background-clip: text;
    background-clip: text;
    color: transparent;
  }
  .title-line--script {
    font-weight: 300;
    font-size: 122px;
    line-height: 98px;
    color: var(--ink-light);
    background: none;
    -webkit-text-fill-color: var(--ink-light);
  }

  .accent-block {
    position: absolute;
    left: 1012px;
    top: 456px;
    width: 188px;
    height: 285px;
    background: linear-gradient(160deg, var(--block-top), var(--block-bottom));
  }

  .subtitle {
    position: absolute;
    top: 1048px;
    left: 0;
    width: 1188px;
    text-align: center;
    font-weight: 600;
    font-size: 35px;
    line-height: 42px;
    letter-spacing: 0.2px;
    color: var(--sub-ink);
  }
</style>
</head>
<body>
  <main class="cover">
    <div class="network-texture" role="img" aria-label="Faint network of connected dots and lines across a pale blue-grey background"></div>

    <p class="author">MARIEKE VOLLEN</p>

    <h1 class="title">
      <span class="title-line">BRIGHT</span>
      <span class="title-line">MAKER'S</span>
      <span class="title-line title-line--script">Manual</span>
    </h1>

    <div class="accent-block" role="img" aria-label="Blue square with a faint glowing network of dots"></div>

    <p class="subtitle">48 IDEAS FOR BUILDING TOOLS AND<br>SERVICES PEOPLE TRULY WANT</p>
  </main>
</body>
</html>
```